Design a modern, classy & professional business card for an online real estate agency, specializing in medium-luxury properties in Thailand and later in Singapore and UK.

Possible design ideas so far: (not essential)

- curved corner(s) to the card, white on front & turquoise on back or visa versa.

- front of card - clear and simple, company name in metallic grey/monochrome, logo graphic & company name on front in spot UV or embossed/debossed effect.

- back of card - large, close-cropped, 'ghost' patterns of the C-shaped curves of logo, or company name repeated on back of card in spot UV.

Target Market(s)

- young to middle-aged professionals mainly (but ideally should design should suit all)

- UK, US,EU,AUS & ASIAN mainly (but ideally should design should suit all countries)

Industry/Entity Type

Real Estate

Requirements
Must have
• THEME:
- Luxurious & Modern
- Clean & striking
- Unique & creative

INFO:
- Logo & company name on front
- Contact details on back:

Tobias Lindqvar
Managing Director

www.velmoraestates.example
www.velmoraestates-uk.example

Tel: 084-273-6190
email: tobias@velmoraestates.example

(contact details can be displayed in any order as suites design.)

Nice to have
• - curved corner(s) to the card, white on front & turquoise on back or visa versa.

Should not have
• - No generic images of properties, palm trees/coconut trees etc.

- No other other bold colors, except for main turquoise, grey, metallic white & black theme.

- No obvious business card templates

```html
<!DOCTYPE html>
<html lang="en">
<head>
<meta charset="utf-8">
<title>Velmora Estates – Business Card</title>
<link rel="stylesheet" href="https://fonts.googleapis.com/css2?family=Tinos&family=Arimo&display=swap">
<style>
  :root {
    --backdrop: #3b3b3b;
    --turquoise: #6dd8d2;
    --turquoise-light: #a9ebe6;
    --turquoise-deep: #3fc4bd;
    --card-grey: #b4b0ad;
    --logo-grey: #767676;
    --ink: #2a1a1a;
    --white: #ffffff;
    --rule: rgba(255,255,255,0.85);
  }
  html, body {
    margin: 0;
    padding: 0;
    width: 1200px;
    height: 889px;
    overflow: hidden;
    background: var(--backdrop);
  }
  .canvas {
    position: relative;
    width: 1200px;
    height: 889px;
  }
  .card {
    position: absolute;
    overflow: hidden;
  }
  .card-bands {
    position: absolute;
    inset: 0;
  }
  .card--front {
    left: 85px;
    top: 62px;
    width: 710px;
    height: 405px;
    border-radius: 52px;
    background: var(--turquoise);
  }
  .card--back {
    left: 427px;
    top: 408px;
    width: 708px;
    height: 402px;
    border-radius: 56px;
    background: var(--card-grey);
  }
  .brand {
    position: absolute;
    display: flex;
    align-items: center;
  }
  .brand-square {
    background: var(--turquoise-deep);
    flex: none;
  }
  .brand-name {
    font-family: "Tinos", serif;
    font-weight: 400;
    color: var(--logo-grey);
    white-space: nowrap;
  }
  .card--front .brand {
    left: 143px;
    top: 144px;
    gap: 18px;
  }
  .card--front .brand-square {
    width: 118px;
    height: 118px;
  }
  .card--front .brand-name {
    font-size: 58px;
  }
  .card--back .brand {
    left: 353px;
    top: 24px;
    gap: 12px;
  }
  .card--back .brand-square {
    width: 76px;
    height: 76px;
  }
  .card--back .brand-name {
    font-size: 36px;
  }
  .ghost-pattern {
    position: absolute;
    left: 0;
    top: 0;
    width: 708px;
    height: 402px;
  }
  .holder {
    position: absolute;
    left: 0;
    right: 0;
    top: 183px;
    text-align: center;
    font-family: "Tinos", serif;
    color: var(--ink);
  }
  .holder-name {
    margin: 0;
    font-size: 37px;
    font-weight: 400;
    line-height: 1.1;
  }
  .holder-title {
    margin: 4px 0 0;
    font-size: 24px;
    line-height: 1.1;
  }
  .contact {
    position: absolute;
    left: 36px;
    right: 40px;
    top: 310px;
    height: 66px;
    border-top: 1px solid var(--rule);
    border-bottom: 1px solid var(--rule);
    font-family: "Arimo", sans-serif;
    font-size: 18px;
    color: var(--white);
    line-height: 23px;
    box-sizing: border-box;
    padding-top: 9px;
    display: flex;
    justify-content: space-between;
  }
  .contact-list, .web-list {
    margin: 0;
    padding: 0;
    list-style: none;
  }
  .contact-label {
    display: inline-block;
    width: 52px;
  }
</style>
</head>
<body>
<main class="canvas">

  <section class="card card--front" aria-label="Card front">
    <svg class="card-bands" viewBox="0 0 710 405" aria-hidden="true">
      <polygon points="330,0 710,0 710,120" fill="var(--turquoise-light)" opacity="0.55"/>
      <polygon points="470,0 710,0 710,60" fill="var(--white)" opacity="0.25"/>
      <polygon points="0,250 0,405 300,405" fill="var(--turquoise-light)" opacity="0.5"/>
      <polygon points="0,270 420,405 0,405" fill="var(--white)" opacity="0.18"/>
      <polygon points="0,330 0,405 180,405" fill="#9fb9b7" opacity="0.35"/>
    </svg>
    <div class="brand">
      <span class="brand-square"></span>
      <span class="brand-name">Velmora Estates</span>
    </div>
  </section>

  <section class="card card--back" aria-label="Card back">
    <svg class="ghost-pattern" viewBox="0 0 708 402" role="img" aria-label="Soft faint turquoise ghost decoration across the card">
      <defs>
        <linearGradient id="ghost-wash" x1="0" y1="1" x2="1" y2="0">
          <stop offset="0" stop-color="var(--card-grey)" stop-opacity="0"/>
          <stop offset="0.55" stop-color="#bcc6c5" stop-opacity="0.6"/>
          <stop offset="1" stop-color="var(--turquoise-light)" stop-opacity="0.9"/>
        </linearGradient>
      </defs>
      <rect width="708" height="402" fill="url(#ghost-wash)"/>
      <polygon points="300,0 708,0 708,110 420,130" fill="var(--turquoise-light)" opacity="0.45"/>
    </svg>
    <div class="brand">
      <span class="brand-square"></span>
      <span class="brand-name">Velmora Estates</span>
    </div>
    <div class="holder">
      <h1 class="holder-name">Tobias Lindqvar</h1>
      <p class="holder-title">Managing Director</p>
    </div>
    <div class="contact">
      <ul class="contact-list">
        <li><span class="contact-label">Tel</span>: 084-273-6190</li>
        <li>email : tobias@velmoraestates.example</li>
      </ul>
      <ul class="web-list">
        <li>www.velmoraestates.example</li>
        <li>www.velmoraestates-uk.example</li>
      </ul>
    </div>
  </section>

</main>
</body>
</html>
```